Business Card Design Project

Hi I am after a business card double sided 1 side to have the attached PDF on front on the back:

Trent Malloway - Managing Director
Mobile: 0413 268 471
email: trent@vrixo.com.au
web: www.vrixo.com.au

Industry/Entity Type

Business

Font styles to use
Sans Serif

Requirements
Must have
• I want a classy looking card
Nice to have
• I like lime green and black and white

```html
<!DOCTYPE html>
<html lang="en">
<head>
<meta charset="utf-8">
<title>Vrixo – Business Card</title>
<link rel="stylesheet" href="https://fonts.googleapis.com/css2?family=Arimo:wght@400;700&family=Questrial&display=swap">
<style>
  :root {
    --lime: #9cfa00;
    --black: #000000;
    --white: #ffffff;
    --ink: #2b2b2b;
    --edge: #8a8a8a;
  }
  * { margin: 0; padding: 0; box-sizing: border-box; }
  html, body {
    width: 1200px; height: 631px; overflow: hidden;
    background: var(--white);
  }
  .sheet {
    position: relative; width: 1200px; height: 631px;
    font-family: "Arimo", Arial, sans-serif;
  }
  .card-shapes { position: absolute; inset: 0; }
  .text { position: absolute; white-space: nowrap; line-height: 1; }

  .brand-mark {
    position: absolute; left: 0; width: 511px;
    display: flex; align-items: center; justify-content: center; gap: 22px;
  }
  .brand-mark .square {
    width: 62px; height: 62px; border-radius: 10px; background: var(--lime);
  }
  .brand-mark .name {
    font-family: "Questrial", "Century Gothic", sans-serif;
    font-size: 62px; font-weight: 400; color: var(--ink); letter-spacing: 1px;
  }
  .front-top { top: 92px; height: 120px; }
  .front-bottom { top: 438px; height: 120px; }

  .web, .email { font-size: 23px; }
  .back-dark .web, .back-dark .email { color: var(--white); left: 720px; }
  .back-lime .web, .back-lime .email { color: var(--black); left: 708px; font-size: 24px; }

  .holder-name {
    right: 63px; font-size: 44px; font-weight: 700; color: var(--lime);
    letter-spacing: -0.5px;
  }
  .holder-role { right: 62px; font-size: 21px; color: var(--lime); }
  .mobile { right: 20px; font-size: 21px; color: var(--lime); }
</style>
</head>
<body>
<div class="sheet">
  <svg class="card-shapes" width="1200" height="631" viewBox="0 0 1200 631">
    <defs>
      <clipPath id="back-lime-clip">
        <rect x="690" y="347" width="510" height="284" rx="20"/>
      </clipPath>
    </defs>
    <!-- front cards -->
    <rect x="1" y="2" width="510" height="283" rx="20" fill="var(--white)" stroke="var(--edge)" stroke-width="1.2"/>
    <rect x="1" y="348" width="510" height="282" rx="20" fill="var(--white)" stroke="var(--edge)" stroke-width="1.2"/>

    <!-- back card, dark version -->
    <rect x="690" y="0" width="510" height="283" rx="20" fill="var(--black)"/>
    <path d="M705 97 C900 93 1110 84 1200 42 L1200 56 C1120 88 930 96 705 97 Z" fill="var(--white)"/>

    <!-- back card, lime version -->
    <g clip-path="url(#back-lime-clip)">
      <rect x="690" y="347" width="510" height="284" fill="var(--black)"/>
      <path d="M690 347 H1200 V386 C1120 424 960 444 690 448 Z" fill="var(--lime)"/>
      <path d="M690 448 C960 444 1120 424 1200 386 V398 C1130 434 970 449 690 450 Z" fill="var(--white)"/>
    </g>
  </svg>

  <div class="brand-mark front-top">
    <span class="square"></span>
    <span class="name">Vrixo</span>
  </div>
  <div class="brand-mark front-bottom">
    <span class="square"></span>
    <span class="name">Vrixo</span>
  </div>

  <div class="back-dark">
    <div class="text web" style="top:25px">www.vrixo.com.au</div>
    <div class="text email" style="top:49px">email: trent@vrixo.com.au</div>
    <div class="text holder-name" style="top:124px">Trent Malloway</div>
    <div class="text holder-role" style="top:173px">Managing Director</div>
    <div class="text mobile" style="top:250px">Mobile: 0413 268 471</div>
  </div>

  <div class="back-lime">
    <div class="text web" style="top:382px">www.vrixo.com.au</div>
    <div class="text email" style="top:407px">email: trent@vrixo.com.au</div>
    <div class="text holder-name" style="top:480px">Trent Malloway</div>
    <div class="text holder-role" style="top:529px">Managing Director</div>
    <div class="text mobile" style="top:582px">Mobile: 0413 268 471</div>
  </div>
</div>
</body>
</html>
```